Design for web app with Plinkora Stratum Craft - Tarvo7 SMS consult

We are developing a web app that will work in browsers. Its main purpose is to allow for users (signing up and logging in with their phone number) to track their habbits and select consultants to whom they can send SMS for help.

The wireframes of the app can be accessed here (pdf):
https://files.plinkora.example/d/7K2mWqLzXv4NtRb9HcJpYsAeUfDg3/view

NB!: Please do not follow the mockups 100% literally, but the Plinkora Stratum craft guidelines.

The technical specifications and descriptions of the web app's functionalities are available in the link below:
https://papers.plinkora.example/doc/4HsTnV8bQeZr2LmXwYcKpDjAuFgN6oRiE5tW1yMx/edit

Requirements for the design:

- The design should be provided as PSD, where each page/section should be in its own PSD file OR all pages/sections should be represented as folder groups in a single PSD file.

- All graphical elements in the design should be delivered as single layers which can then be extracted from the PSD.

- All graphical elements (icons, graphical buttons, etc.) should be provided as vector objects in the PSD, so that they can be exported into different sizes without loss of quality (for responsiveness).

- The design should use either web safe fonts or Plinkora Type.

Instructions for the design:
The design should be based on Plinkora Stratum Craft - http://www.plinkora.example/craft/spec/stratum-craft/overview.html

Please also provide an app icon and suggest a logo for the app.

Requirements
Must have
• Based on Plinkora Stratum Craft
• Flat
Nice to have
• Nice looking and not so stiff as the default Plinkora Stratum Craft, but it is important to follow their guidelines.
Should not have
• 3D

```html
<!DOCTYPE html>
<html lang="en">
<head>
<meta charset="utf-8">
<title>Tarvo7 – Send SMS</title>
<link rel="stylesheet" href="https://fonts.googleapis.com/css2?family=Open+Sans:wght@300;400;600&family=Luckiest+Guy&display=swap">
<style>
  :root {
    --status-bar: #0f1d31;
    --bg-top: #775139;
    --bg-bottom: #4e2808;
    --bg-sweep: rgba(255, 235, 215, 0.08);
    --text-light: #f3ebe4;
    --field-bg: #e1d9d5;
    --field-text: #2a2320;
    --brand-blue: #1a78b4;
    --send-green: #4f8b41;
    --cancel-red: #8a140f;
    --button-edge: #8a7440;
    --white: #ffffff;
  }
  * { box-sizing: border-box; margin: 0; padding: 0; }
  html, body { width: 720px; height: 1200px; overflow: hidden; }
  body {
    position: relative;
    font-family: "Open Sans", Arial, sans-serif;
    background: linear-gradient(180deg, var(--bg-top) 0%, #6a3f22 45%, var(--bg-bottom) 100%);
    color: var(--text-light);
  }
  .background-sweep { position: absolute; inset: 0; width: 720px; height: 1200px; }
  .status-bar {
    position: absolute; top: 0; left: 0; width: 720px; height: 30px;
    background: var(--status-bar); color: var(--white);
    font-size: 21px; line-height: 30px; text-align: center;
  }
  .status-bar .signal { position: absolute; left: 6px; top: 9px; }
  .status-bar .battery { position: absolute; right: 14px; top: 8px; }
  .brand {
    position: absolute; left: 65px; top: 84px;
    display: flex; align-items: center; gap: 12px;
  }
  .brand-square { width: 24px; height: 24px; background: var(--brand-blue); }
  .brand-name { font-size: 36px; font-weight: 400; color: var(--white); letter-spacing: 1px; }
  .prompt {
    position: absolute; left: 0; top: 336px; width: 720px;
    text-align: center; font-size: 22px; font-weight: 300; line-height: 48px;
  }
  .recipient-line {
    position: absolute; left: 198px; top: 476px; width: 261px; height: 2px;
    background: var(--text-light);
  }
  .sms-field {
    position: absolute; left: 121px; top: 502px; width: 457px; height: 293px;
    background: var(--field-bg); color: var(--field-text);
    font-size: 22px; font-weight: 400; padding: 14px 34px;
  }
  .action {
    position: absolute; width: 218px; height: 60px;
    border: 2px solid var(--button-edge); border-radius: 10px;
    color: var(--white); font-family: "Luckiest Guy", Impact, sans-serif;
    font-size: 25px; letter-spacing: 1.5px;
    display: flex; align-items: center; justify-content: center; padding-top: 4px;
  }
  .action-send { left: 236px; top: 882px; background: var(--send-green); }
  .action-cancel { left: 233px; top: 998px; width: 220px; background: var(--cancel-red); }
</style>
</head>
<body>
  <svg class="background-sweep" viewBox="0 0 720 1200" aria-hidden="true">
    <path d="M360 30 C560 180 680 620 710 1200 L720 1200 L720 30 Z" fill="var(--bg-sweep)"/>
  </svg>

  <header class="status-bar">
    <svg class="signal" width="66" height="14" viewBox="0 0 66 14" aria-hidden="true">
      <circle cx="7" cy="7" r="6" fill="#000"/>
      <circle cx="21" cy="7" r="6" fill="#000"/>
      <circle cx="35" cy="7" r="6" fill="#000"/>
      <circle cx="49" cy="7" r="6" fill="#fff"/>
    </svg>
    <span class="clock">10:00 AM</span>
    <svg class="battery" width="40" height="16" viewBox="0 0 40 16" aria-hidden="true">
      <rect x="1" y="1" width="34" height="14" fill="none" stroke="#fff" stroke-width="2"/>
      <rect x="4" y="4" width="20" height="8" fill="#fff"/>
      <rect x="36" y="5" width="3" height="6" fill="#fff"/>
    </svg>
  </header>

  <div class="brand">
    <span class="brand-square"></span>
    <span class="brand-name">Tarvo7</span>
  </div>

  <p class="prompt">Please write the text for the SMS and<br>confirm that youwant to send it to</p>
  <div class="recipient-line"></div>

  <div class="sms-field">SMS Text...</div>

  <div class="action action-send">SEND</div>
  <div class="action action-cancel">CANCEL</div>
</body>
</html>
```